Full A4 Page Magazine Advertisement

We are a staircase and balustrade manufacturer established for 30 years that are very well known within the Perth building trade as producing the best quality workmanship, for using the best quality materials and for excellent customer service. We are traditionally known for our timber products but have also been manufacturing in steel for some 15 years which even some of the trade are unaware of. I need a new full page glossy magazine advert to communicate primarily to end users who are not generally aware of us or our reputation; the quality of our products and craftsmanship; the fact that we can manufacture staircases, balustrades and handrails, (with the emphasis on our steel staircases); our ability to manufacture in steel, timber, glass or stainless steel or any combination of these materials; our ability to manufacture modern, traditional or classical styles; our trustworthy service and excellent customer service; our comprehensive showroom facility with a full display of staircases, balustrading and handrails in all materials. Would like the page colour (if any) to be black; emphasis on the steel staircase image; logo with all contact details; The final design should emphasise our quality, dependability & flexibility of what we can do.

Industry/Entity Type

Building

```html
<!DOCTYPE html>
<html lang="en">
<head>
<meta charset="utf-8">
<title>Summit Stairs – Staircases, Balustrades, Handrails</title>
<link href="https://fonts.googleapis.com/css2?family=Oswald:wght@500;700&family=Roboto:wght@300;400&display=swap" rel="stylesheet">
<style>
  :root {
    --wall-purple: #3b3673;
    --wall-deep: #25224d;
    --timber: #6b3a22;
    --light: #e9ecef;
    --white: #ffffff;
    --yellow: #ffd200;
    --ink: #2b2b2b;
    --grey-text: #5a5a5a;
    --footer: #26262a;
  }
  * { margin: 0; padding: 0; box-sizing: border-box; }
  html, body { width: 848px; height: 1200px; overflow: hidden; background: var(--white); }
  .advert { position: relative; width: 848px; height: 1200px; overflow: hidden; }
  .hero-photo { position: absolute; inset: 0; width: 848px; height: 1200px; }
  .overlay { position: absolute; inset: 0; width: 848px; height: 1200px; }

  .headline {
    position: absolute; left: 150px; top: 452px; width: 380px;
    text-align: center; font-family: "Oswald", sans-serif; font-weight: 700;
    text-transform: uppercase; line-height: 1;
    text-shadow: 0 2px 6px rgba(0,0,0,.55);
  }
  .headline .intro { display: block; color: var(--yellow); font-size: 29px; letter-spacing: .5px; margin-bottom: 4px; }
  .headline .product { display: block; color: var(--white); font-size: 54px; letter-spacing: .5px; line-height: 1.02; }

  .showroom {
    position: absolute; left: 84px; top: 988px;
    display: flex; gap: 16px; align-items: flex-start;
  }
  .showroom svg { width: 22px; height: 30px; margin-top: 4px; }
  .showroom address {
    font-style: normal; font-family: "Roboto", sans-serif; font-weight: 400;
    font-size: 18px; line-height: 1.33; color: var(--grey-text);
  }

  .brand {
    position: absolute; left: 530px; top: 968px; width: 280px;
    display: flex; align-items: center; justify-content: center; gap: 12px;
  }
  .brand .mark { width: 22px; height: 22px; background: var(--ink); }
  .brand .name {
    font-family: "Oswald", sans-serif; font-weight: 500; font-size: 32px;
    letter-spacing: 2px; color: var(--ink); text-transform: uppercase;
  }

  .contact-bar {
    position: absolute; left: 0; top: 1096px; width: 848px; height: 104px;
    background: var(--footer); border-top: 5px solid var(--yellow);
    display: flex; align-items: center; justify-content: space-between;
    padding: 0 46px 30px 50px;
    font-family: "Roboto", sans-serif; font-weight: 300; font-size: 17px; color: var(--white);
  }
  .contact-bar .item { display: flex; align-items: center; gap: 12px; }
  .contact-bar svg { width: 26px; height: 26px; }
</style>
</head>
<body>
<main class="advert">
  <svg class="hero-photo" viewBox="0 0 848 1200" role="img" aria-label="Photograph of a floating timber staircase with frameless glass balustrade and stainless steel handrail against a textured purple feature wall">
    <defs>
      <linearGradient id="wallTone" x1="0" y1="0" x2="1" y2="0.4">
        <stop offset="0" stop-color="#2f2b62"/>
        <stop offset="0.5" stop-color="#3b3673"/>
        <stop offset="0.72" stop-color="#6f6f8c"/>
        <stop offset="1" stop-color="#e6e9ec"/>
      </linearGradient>
      <linearGradient id="stairTone" x1="0" y1="1" x2="1" y2="0">
        <stop offset="0" stop-color="#4a2414" stop-opacity=".9"/>
        <stop offset="0.6" stop-color="#7a4127" stop-opacity=".75"/>
        <stop offset="1" stop-color="#8a4a2a" stop-opacity="0"/>
      </linearGradient>
    </defs>
    <rect width="848" height="1200" fill="url(#wallTone)"/>
    <polygon points="220,1100 380,820 560,520 700,330 848,250 848,520 640,860 520,1100" fill="url(#stairTone)"/>
  </svg>

  <svg class="overlay" viewBox="0 0 848 1200" aria-hidden="true">
    <polygon points="0,520 405,145 405,405 0,720" fill="#ffffff" opacity=".14"/>
    <polygon points="170,240 405,145 405,260 170,360" fill="#ffffff" opacity=".12"/>
    <polygon points="0,890 340,890 372,1096 0,1096" fill="#ffffff"/>
    <polygon points="848,770 848,1096 340,1096 560,975" fill="#ffffff"/>
    <polygon points="0,888 345,888 348,900 0,900" fill="#ffffff" opacity=".6"/>
  </svg>

  <h1 class="headline">
    <span class="intro">Manufacturers of</span>
    <span class="product">Staircases</span>
    <span class="product">Balustrades</span>
    <span class="product">Handrails</span>
  </h1>

  <div class="showroom">
    <svg viewBox="0 0 22 30" aria-hidden="true">
      <path d="M11 1C5.5 1 1 5.4 1 10.8 1 18 11 29 11 29s10-11 10-18.2C21 5.4 16.5 1 11 1z" fill="#5a5a5a"/>
      <circle cx="11" cy="10.5" r="4" fill="#ffffff"/>
    </svg>
    <address>
      Summit Stairs<br>
      Factory &amp; Showrooms<br>
      17 Kestrel Road<br>
      Rivervale WA 6103
    </address>
  </div>

  <div class="brand">
    <span class="mark"></span>
    <span class="name">Summit Stairs</span>
  </div>

  <footer class="contact-bar">
    <div class="item">
      <svg viewBox="0 0 26 26" aria-hidden="true">
        <rect x="2" y="6" width="22" height="15" rx="1.5" fill="#ffd200"/>
        <path d="M3 7l10 8 10-8" fill="none" stroke="#26262a" stroke-width="1.6"/>
      </svg>
      <span>sales@summitstairs.com.au</span>
    </div>
    <div class="item">
      <svg viewBox="0 0 26 26" aria-hidden="true">
        <path d="M7 3c1 0 3.5 4 3.5 5s-2 2-2 3c0 1.5 4 5.5 5.5 5.5 1 0 2-2 3-2s5 2.5 5 3.5c0 2-3 4.5-5 4.5C11 23 3 15 3 8c0-2 2.5-5 4-5z" fill="#ffd200"/>
      </svg>
      <span>(08) 9000 4182</span>
    </div>
    <div class="item">
      <svg viewBox="0 0 26 26" aria-hidden="true">
        <circle cx="13" cy="13" r="11" fill="#ffd200"/>
        <ellipse cx="13" cy="13" rx="5" ry="11" fill="none" stroke="#26262a" stroke-width="1.4"/>
        <path d="M2 13h22M4 7.5h18M4 18.5h18" stroke="#26262a" stroke-width="1.4"/>
      </svg>
      <span>www.summitstairs.com.au</span>
    </div>
  </footer>
</main>
</body>
</html>
```